Specialised investor in e-mobility and energy wants business card design

We need a business card design that fits our existing corporate design. <The look and feel must be 'sharp'/'clean', dynamic, communicate momentum, professionalism etc (as one would imagine from a firm in the financial sector). We like the idea of a reverse-side of the card that includes the logo, and the name and contact details on the other. We expect the deliverable to be whatever format might be required to be able to get cards printed directly by a service such as tandor press. Our website is www.orm.capital

```html
<!DOCTYPE html>
<html lang="en">
<head>
<meta charset="utf-8">
<title>ORM Capital – Business Card</title>
<link rel="stylesheet" href="https://fonts.googleapis.com/css2?family=Montserrat:wght@400;500;700&display=swap">
<style>
  :root {
    --backdrop: #2b2d31;
    --card: #ffffff;
    --green-dark: #355426;
    --green-light: #86b54a;
    --green-wash: #e7f0dc;
    --text-grey: #6b6b6b;
  }
  * { margin: 0; padding: 0; box-sizing: border-box; }
  html, body {
    width: 1200px; height: 952px; overflow: hidden;
    background: var(--backdrop);
    font-family: "Montserrat", sans-serif;
  }
  .stage {
    position: relative; width: 1200px; height: 952px;
    display: flex; align-items: center; justify-content: center; gap: 48px;
  }
  .card {
    position: relative; width: 525px; height: 300px;
    background: var(--card);
    box-shadow: 0 14px 30px rgba(0,0,0,.45);
    overflow: hidden;
  }
  .wordmark {
    display: flex; align-items: center; gap: 10px;
    color: var(--green-dark); font-weight: 500; letter-spacing: .5px;
    white-space: nowrap;
  }
  .wordmark__square {
    width: 14px; height: 14px; background: var(--green-dark); flex: none;
  }
  /* front side */
  .card--front .wordmark {
    position: absolute; top: 36px; left: 190px; font-size: 28px;
  }
  .contact-list {
    position: absolute; left: 26px; top: 110px;
    list-style: none; display: grid; gap: 9px;
    font-size: 11.5px; color: var(--text-grey);
    z-index: 1;
  }
  .contact-list li { display: flex; align-items: center; gap: 9px; white-space: nowrap; }
  .contact-list svg { width: 16px; height: 16px; flex: none; }
  .holder {
    position: absolute; right: 34px; top: 132px; text-align: right; z-index: 1;
  }
  .holder__name {
    font-size: 18px; font-weight: 700; color: var(--green-light); letter-spacing: .5px;
  }
  .holder__role { font-size: 11.5px; color: var(--text-grey); margin-top: 2px; }
  .brand-decoration {
    position: absolute; left: 200px; bottom: 0; width: 210px; height: 150px;
    background: linear-gradient(160deg, rgba(231,240,220,0) 0%, var(--green-wash) 55%, #d6e6c4 100%);
  }
  /* back side */
  .card--back { display: flex; align-items: center; justify-content: center; }
  .card--back .wordmark { font-size: 40px; }
  .card--back .wordmark__square { width: 20px; height: 20px; }
</style>
</head>
<body>
<main class="stage">
  <section class="card card--front" aria-label="Card front">
    <div class="wordmark"><span class="wordmark__square"></span>ORM Capital</div>
    <ul class="contact-list">
      <li>
        <svg viewBox="0 0 16 16"><rect width="16" height="16" rx="2" fill="#86b54a"/><path d="M5 4l2 0 1 2.5-1.2 1a6 6 0 0 0 2.7 2.7l1-1.2L13 10v2c-4.5 0-8-3.5-8-8z" fill="#fff"/></svg>
        +41 79 555 0142
      </li>
      <li>
        <svg viewBox="0 0 16 16"><rect width="16" height="16" rx="2" fill="#86b54a"/><rect x="3.5" y="5" width="9" height="6.5" fill="none" stroke="#fff" stroke-width="1.2"/><path d="M3.5 5l4.5 3.5L12.5 5" fill="none" stroke="#fff" stroke-width="1.2"/></svg>
        lena@orm.capital
      </li>
      <li>
        <svg viewBox="0 0 16 16"><rect width="16" height="16" rx="2" fill="#86b54a"/><path d="M8 13s-3.5-3.8-3.5-6.3a3.5 3.5 0 0 1 7 0C11.5 9.2 8 13 8 13z" fill="#fff"/><circle cx="8" cy="6.7" r="1.3" fill="#86b54a"/></svg>
        Morvel, Switzerland
      </li>
      <li>
        <svg viewBox="0 0 16 16"><rect width="16" height="16" rx="2" fill="#86b54a"/><path d="M4 12L12 4M7 4h5v5" fill="none" stroke="#fff" stroke-width="1.5"/></svg>
        www.orm.capital
      </li>
    </ul>
    <div class="holder">
      <p class="holder__name">LENA HART</p>
      <p class="holder__role">Manager</p>
    </div>
    <div class="brand-decoration" role="img" aria-label="Large brand mark decoration in dark and light green"></div>
  </section>

  <section class="card card--back" aria-label="Card back">
    <div class="wordmark"><span class="wordmark__square"></span>ORM Capital</div>
  </section>
</main>
</body>
</html>
```